Talvero

I'd like new business card design options. I'll need to provide updated contact info although after the deign is complete. We are in IT, specifically in the data backup, archiving and disaster recovery verticals.

Business

```html
<!DOCTYPE html>
<html lang="en">
<head>
<meta charset="utf-8">
<title>Talvero — Business Card</title>
<link rel="stylesheet" href="https://fonts.googleapis.com/css2?family=Arimo:wght@400;700&display=swap">
<style>
  :root {
    --page-bg: #e9e9ea;
    --card-white: #ffffff;
    --card-shade: #eeeff1;
    --brand-blue: #1c74c8;
    --band-blue: #1662ad;
    --band-light: #3ea3e0;
    --text-grey: #6d6f73;
    --text-light: #a3a5a9;
    --band-text: #ffffff;
  }
  * { margin: 0; padding: 0; box-sizing: border-box; }
  html, body { width: 1200px; height: 600px; overflow: hidden; }
  body {
    background: var(--page-bg);
    font-family: "Arimo", Arial, sans-serif;
    display: flex; align-items: center; justify-content: center;
  }
  .card {
    position: relative;
    width: 840px; height: 480px;
    border-radius: 30px;
    overflow: hidden;
    background: radial-gradient(ellipse at 35% 40%, var(--card-white) 40%, var(--card-shade) 100%);
    box-shadow: 0 10px 30px rgba(0,0,0,0.12);
  }
  .brand {
    position: absolute; left: 56px; top: 130px;
    display: flex; align-items: center; gap: 18px;
  }
  .brand-dot {
    width: 60px; height: 60px; border-radius: 50%;
    background: var(--brand-blue);
  }
  .brand-name {
    font-size: 50px; font-weight: 700; letter-spacing: 6px;
    color: var(--brand-blue); line-height: 1;
  }
  .providers {
    position: absolute; left: 56px; bottom: 88px;
    color: var(--text-light); font-size: 16px; line-height: 1.35;
  }
  .contact {
    position: absolute; left: 450px; top: 96px; width: 370px;
  }
  .contact-name {
    font-size: 21px; font-weight: 700; color: var(--brand-blue);
    letter-spacing: 0.3px; white-space: nowrap;
  }
  .contact-title {
    font-size: 15px; color: var(--text-grey); margin-top: 6px; letter-spacing: 0.5px;
  }
  .contact-list { list-style: none; margin-top: 22px; }
  .contact-list li {
    display: flex; align-items: center; gap: 10px;
    font-size: 15px; color: var(--text-grey); line-height: 1.65;
  }
  .contact-list svg { width: 14px; height: 14px; fill: var(--band-blue); flex: none; }
  .address {
    margin-top: 20px; font-size: 15px; color: var(--text-grey); line-height: 1.5;
  }
  .band-edge {
    position: absolute; left: 0; right: 0; bottom: 56px; height: 10px;
    background: var(--band-light);
  }
  .services-band {
    position: absolute; left: 0; right: 0; bottom: 0; height: 56px;
    background: var(--band-blue);
    color: var(--band-text);
    font-size: 17px; letter-spacing: 0.5px;
    display: flex; align-items: center; justify-content: center;
  }
</style>
</head>
<body>
  <article class="card">
    <div class="brand">
      <span class="brand-dot"></span>
      <div class="brand-name">TALVERO</div>
    </div>

    <p class="providers">PROVIDERS OF<br>VaultDesk™ and RackVault™</p>

    <section class="contact">
      <h1 class="contact-name">MARCUS L. DEVEREAUX, Ph.D.</h1>
      <p class="contact-title">PRESIDENT, CTO</p>
      <ul class="contact-list">
        <li>
          <svg viewBox="0 0 16 16" aria-hidden="true"><path d="M3.5 1l2.5 3-1.5 2c1 2 3 4 5 5l2-1.5 3 2.5-1.5 2.5C8 14.5 1.5 8 1 3z"/></svg>
          555.214.3871
        </li>
        <li>
          <svg viewBox="0 0 16 16" aria-hidden="true"><path d="M4 1h8v14H4zM5.5 3v9h5V3z"/></svg>
          555.406.9152
        </li>
        <li>
          <svg viewBox="0 0 16 16" aria-hidden="true"><path d="M1 3h14v10H1zM2.5 4.5L8 9l5.5-4.5z"/></svg>
          marcus.devereaux@talvero.com
        </li>
        <li>
          <svg viewBox="0 0 16 16" aria-hidden="true"><path d="M8 1a7 7 0 100 14A7 7 0 008 1zm0 1.5a5.5 5.5 0 110 11 5.5 5.5 0 010-11zM2.5 7.3h11v1.4h-11zM7.3 2.5h1.4v11H7.3z"/></svg>
          www.talvero.com
        </li>
      </ul>
      <p class="address">402 North Calloway Street<br>Brenford, Texas 75210</p>
    </section>

    <div class="band-edge"></div>
    <footer class="services-band">ONLINE PC BACKUP | CONTINUOUS SERVER BACKUP | DATA ARCHIVING</footer>
  </article>
</body>
</html>
```